Name Card Design

Looking to create a card for my business. I am a personal stylist, my business is clothes, shoes and everything to do with looking fashion forward. I help people achieve the most polished look with cloths and grooming. I would like my card to be a reflection of my qualities which are: poise, elegance, creativity and fairness.
Things I like a simple yet expensive looking, sometimes less simple but highly creative and different catches my eye. For instance I saw a card with lace trimming at the bottom, it made me think about the business that person was in. I don't like childish designs with butterflies, trees, flowers, etc.
Here is my site www.Marta-Venn.example for your perusal

On the card it should have the following info
Marta Venn
personal stylist
www.Marta-Venn.example
(+65) 842-30587
Facebook page: Ringtochic

Back of the card:
Wardrobe weeding
Personal shopping
Style consultation

Target Market(s)

mostly working women

Industry/Entity Type

Fashion

Font styles to use
Serif
Sans Serif

Requirements
Should not have
• butterflies, flowers, feathers, etc

```html
<!DOCTYPE html>
<html lang="en">
<head>
<meta charset="utf-8">
<title>Marta Venn — Name Card</title>
<link rel="stylesheet" href="https://fonts.googleapis.com/css2?family=Arimo:wght@400;700&family=Cormorant+Garamond:wght@500;600&display=swap">
<style>
  :root {
    --backdrop: #e6e4e0;
    --card-black: #050505;
    --card-gloss: #2c2c2c;
    --band-light: #e9e9e9;
    --band-shade: #bdbdbd;
    --ink-white: #f4f4f4;
    --ink-soft: #cfcfcf;
    --band-ink: #2a2a2a;
  }
  * { margin: 0; padding: 0; box-sizing: border-box; }
  html, body { width: 1200px; height: 600px; overflow: hidden; }
  body {
    background: var(--backdrop);
    display: flex;
    align-items: center;
    justify-content: center;
    gap: 60px;
  }
  .card {
    position: relative;
    width: 520px;
    height: 297px;
    border-radius: 14px;
    overflow: hidden;
    background:
      linear-gradient(125deg, transparent 35%, rgba(255,255,255,0.10) 48%, transparent 62%),
      radial-gradient(ellipse at 40% 30%, var(--card-gloss) 0%, var(--card-black) 65%);
    box-shadow: 0 10px 28px rgba(0,0,0,0.35);
    color: var(--ink-white);
  }
  .card__band {
    position: absolute;
    left: 0; right: 0; bottom: 0;
    height: 34px;
    padding: 0 16px;
    background: linear-gradient(180deg, var(--band-light) 0%, #f7f7f7 50%, var(--band-shade) 100%);
    display: flex;
    align-items: center;
    justify-content: center;
  }
  .services {
    font-family: "Cormorant Garamond", serif;
    font-weight: 500;
    font-size: 12px;
    letter-spacing: 0.8px;
    text-transform: uppercase;
    color: var(--band-ink);
    white-space: nowrap;
  }
  .wordmark {
    position: absolute;
    font-family: "Arimo", sans-serif;
    line-height: 1;
  }
  .wordmark__name {
    display: block;
    font-weight: 700;
    font-size: 48px;
    letter-spacing: -1.5px;
    color: var(--ink-white);
  }
  .wordmark__role {
    display: block;
    font-weight: 400;
    font-size: 12px;
    color: var(--ink-soft);
    text-align: right;
    margin-top: 2px;
  }
  .card--front .wordmark { left: 36px; top: 44px; }
  .card--back .wordmark { left: 50%; top: 50%; transform: translate(-50%, -70%); }
  .contact {
    position: absolute;
    left: 200px;
    top: 130px;
    font-family: "Cormorant Garamond", serif;
    color: var(--ink-white);
  }
  .contact__name {
    font-weight: 600;
    font-size: 17px;
    font-variant: small-caps;
    letter-spacing: 1px;
  }
  .contact__title {
    font-weight: 500;
    font-size: 13px;
    text-transform: uppercase;
    letter-spacing: 1px;
    color: var(--ink-soft);
    margin-bottom: 12px;
  }
  .contact__list { list-style: none; }
  .contact__item {
    display: flex;
    align-items: center;
    gap: 8px;
    font-weight: 500;
    font-size: 13px;
    letter-spacing: 0.8px;
    text-transform: uppercase;
    line-height: 20px;
  }
  .contact__icon { width: 12px; height: 12px; flex: none; }
</style>
</head>
<body>
  <section class="card card--front" aria-label="Card front">
    <div class="wordmark">
      <span class="wordmark__name">Marta Venn</span>
      <span class="wordmark__role">image &amp; brand consultant</span>
    </div>
    <div class="contact">
      <p class="contact__name">Marta Venn</p>
      <p class="contact__title">Personal Stylist</p>
      <ul class="contact__list">
        <li class="contact__item">
          <svg class="contact__icon" viewBox="0 0 12 12" aria-hidden="true"><path d="M1 4 Q6 0 11 4 L9.5 5.5 L8 4.5 L8 3.5 Q6 3 4 3.5 L4 4.5 L2.5 5.5 Z M3 6 H9 L10 11 H2 Z" fill="#f4f4f4"/></svg>
          (+65) 842-30587
        </li>
        <li class="contact__item">
          <svg class="contact__icon" viewBox="0 0 12 12" aria-hidden="true"><rect x="1" y="1" width="10" height="10" rx="1.5" fill="#f4f4f4"/></svg>
          Ringtochic
        </li>
        <li class="contact__item">
          <svg class="contact__icon" viewBox="0 0 12 12" aria-hidden="true"><rect x="1.5" y="2" width="9" height="8" fill="none" stroke="#f4f4f4" stroke-width="1"/></svg>
          www.Marta-Venn.example
        </li>
      </ul>
    </div>
    <div class="card__band"></div>
  </section>

  <section class="card card--back" aria-label="Card back">
    <div class="wordmark">
      <span class="wordmark__name">Marta Venn</span>
      <span class="wordmark__role">image &amp; brand consultant</span>
    </div>
    <div class="card__band">
      <p class="services">Wardrobe Weeding | Personal Shopping | Style Consultation</p>
    </div>
  </section>
</body>
</html>
```